Industrial Professional Business Card Design (Vantrel Systems)

Would like professional looking business cards. Not too busy leaning towards minimal. Should have a slogan like:
"Industrial Automation and Control".

We are a tech company that programs industrial PLC computers. We also develop custom hardware solutions. Please use the logo for inspiration.

Target Market(s)

Mining, industrial, processing, automation, factory

Industry/Entity Type

Engineering

Contact Information for Business Card

Name, phone, email, website. job title.

Font styles to use
Other font styles liked:
• droid sans

Requirements
Must have
• Use colours that go well with the logo. Not too busy design.

```html
<!DOCTYPE html>
<html lang="en">
<head>
<meta charset="utf-8">
<title>Vantrel Systems – Business Card</title>
<link href="https://fonts.googleapis.com/css2?family=Open+Sans:wght@400;600&display=swap" rel="stylesheet">
<style>
  :root {
    --canvas-bg: #1b1e22;
    --front-blue: #3d88a8;
    --front-blue-light: #4a95b4;
    --back-blue: #1f6a96;
    --back-blue-deep: #174f74;
    --accent-orange: #e8692a;
    --text-light: #eef3f6;
    --text-soft: #d6e4ec;
  }
  * { box-sizing: border-box; margin: 0; padding: 0; }
  html, body {
    width: 1200px; height: 900px; overflow: hidden;
    background: var(--canvas-bg);
    font-family: "Open Sans", "Droid Sans", sans-serif;
  }
  .canvas {
    width: 1200px; height: 900px;
    display: flex; flex-direction: column; align-items: center; justify-content: center;
    gap: 36px;
  }
  .card {
    position: relative;
    width: 700px; height: 400px;
    overflow: hidden;
    border-radius: 3px;
    box-shadow: 0 14px 30px rgba(0,0,0,0.45);
  }

  /* Front */
  .card-front {
    background: radial-gradient(ellipse at 60% 55%, var(--front-blue-light), var(--front-blue) 70%);
  }
  .brand {
    position: absolute; display: flex; align-items: center; gap: 10px;
    color: var(--text-light); font-weight: 400; letter-spacing: 0.5px;
  }
  .brand-dot {
    border-radius: 50%; background: var(--accent-orange); flex: none;
  }
  .card-front .brand { left: 70px; top: 56px; font-size: 30px; }
  .card-front .brand-dot { width: 22px; height: 22px; }
  .divider {
    position: absolute; left: 70px; top: 232px; width: 520px; height: 3px;
    background: var(--accent-orange);
  }
  .edge-tab {
    position: absolute; right: 0; top: 232px; width: 12px; height: 40px;
    background: var(--accent-orange);
  }
  .holder-name {
    position: absolute; right: 110px; top: 182px;
    font-size: 40px; font-weight: 400; color: var(--text-light);
  }
  .holder-title {
    position: absolute; right: 110px; top: 242px;
    font-size: 20px; color: var(--text-light);
  }
  .contact-list {
    position: absolute; left: 70px; top: 270px; list-style: none;
    color: var(--text-soft); font-size: 15px;
  }
  .contact-list li { display: flex; align-items: center; gap: 10px; height: 26px; }
  .contact-list svg { width: 16px; height: 16px; flex: none; }
  .bottom-strip {
    position: absolute; left: 0; bottom: 0; width: 100%; height: 12px;
    background: var(--accent-orange);
  }

  /* Back */
  .card-back { background: var(--back-blue); }
  .pattern-fill {
    position: absolute; inset: 0;
    background: radial-gradient(ellipse at 50% 40%, var(--back-blue), var(--back-blue-deep) 90%);
  }
  .card-back .brand {
    left: 0; right: 0; top: 120px; justify-content: center; font-size: 40px;
  }
  .card-back .brand-dot { width: 28px; height: 28px; }
  .slogan-band {
    position: absolute; left: 0; right: 0; top: 290px; height: 48px;
    background: var(--accent-orange);
    border-top: 3px solid var(--text-light);
    display: flex; align-items: center; justify-content: center;
    color: var(--text-light); font-size: 26px; letter-spacing: 0.5px;
  }
</style>
</head>
<body>
<main class="canvas">
  <section class="card card-front" aria-label="Business card front">
    <div class="brand"><span class="brand-dot"></span><span>Vantrel Systems</span></div>
    <div class="holder-name">Talia Moyo</div>
    <div class="divider"></div>
    <div class="edge-tab"></div>
    <div class="holder-title">CEO</div>
    <ul class="contact-list">
      <li>
        <svg viewBox="0 0 16 16" aria-hidden="true"><path d="M4 1.5l2.2 3-1.3 1.6a8 8 0 0 0 5 5l1.6-1.3 3 2.2-1.3 2.3C8.5 14.3 1.7 7.5 1.7 2.8z" fill="none" stroke="#d6e4ec" stroke-width="1.2"/></svg>
        <span>5550-318-204</span>
      </li>
      <li>
        <svg viewBox="0 0 16 16" aria-hidden="true"><rect x="1.5" y="3.5" width="13" height="9" fill="none" stroke="#d6e4ec" stroke-width="1.2"/><path d="M1.5 3.5l6.5 5 6.5-5" fill="none" stroke="#d6e4ec" stroke-width="1.2"/></svg>
        <span>hello@vantrelsystems.com</span>
      </li>
      <li>
        <svg viewBox="0 0 16 16" aria-hidden="true"><path d="M8 15s5-5.2 5-9a5 5 0 0 0-10 0c0 3.8 5 9 5 9z" fill="none" stroke="#d6e4ec" stroke-width="1.2"/><circle cx="8" cy="6" r="1.8" fill="#d6e4ec"/></svg>
        <span>14 Corran Road, Eastvale, Harare</span>
      </li>
    </ul>
    <div class="bottom-strip"></div>
  </section>

  <section class="card card-back" aria-label="Business card back">
    <div class="pattern-fill" role="img" aria-label="Faint repeating gear pattern in deep blue tones"></div>
    <div class="brand"><span class="brand-dot"></span><span>Vantrel Systems</span></div>
    <div class="slogan-band">Industrial Automation and Control</div>
  </section>
</main>
</body>
</html>
```